Trellwick Partners Needs a new flyer

We are in need of an update marketing flyer. I have attached a PDF of our standard pitch deck which is used to present to anyone who has never heard of Trellwick Partners. Please use this as your source material to design the brochure.

Also feel free to add additional graphics as you see fit for a well designed and easy to read and understand flyer.

The finish size is 8.5" x 11" so please include a 1/8" lead as this will be professionally printed.

Lastly, I have also attached our logo.

```html
<!DOCTYPE html>
<html lang="en">
<head>
<meta charset="utf-8">
<title>Trellwick Partners – Brochure</title>
<link rel="stylesheet" href="https://fonts.googleapis.com/css2?family=Montserrat:ital,wght@0,300;0,400;0,600;0,700;1,600;1,700&family=Open+Sans:ital,wght@0,400;0,600;0,700;1,600&display=swap">
<style>
:root{
  --navy:#172c78;
  --blue:#213f98;
  --royal:#2a4eab;
  --sky:#1e8fd8;
  --ink:#3b3f4a;
  --muted:#6b7280;
  --paper:#ffffff;
  --mist:#eef2f8;
  --stage:#ebebeb;
}
*{box-sizing:border-box;margin:0;padding:0}
html,body{width:1200px;height:2666px;overflow:hidden}
body{background:var(--stage);font-family:"Open Sans",Arial,sans-serif;color:var(--ink);position:relative}

.spread{position:absolute;display:flex;box-shadow:0 10px 30px rgba(0,0,0,.18)}
.page{position:relative;overflow:hidden;background:var(--paper)}
.page + .page{box-shadow:inset 14px 0 18px -14px rgba(0,0,0,.25)}

/* brand */
.brand{font-family:"Montserrat",Arial,sans-serif;font-weight:600;letter-spacing:.04em;text-transform:uppercase;color:var(--navy);display:flex;align-items:center;gap:.35em;white-space:nowrap}
.brand::after{content:"";width:.55em;height:.55em;background:var(--sky)}
.brand--light{color:#fff}
.tagline{font-family:"Montserrat",Arial,sans-serif;font-weight:700;font-size:.42em;letter-spacing:.08em;color:var(--navy);text-transform:uppercase}
.tagline--light{color:#fff}

.photo{position:absolute}

/* cover */
.cover{position:absolute;inset:0}
.cover .photo{inset:0;background:linear-gradient(135deg,#a4624c 0%,#c9a08c 30%,#8f8e93 55%,#4b4d57 100%)}
.cover-band{position:absolute;top:0;bottom:0;left:52%;right:0;background:rgba(30,55,150,.9)}
.cover-logo{position:absolute;top:7%;left:40%;width:55%;padding:.8em .9em;background:#fff;display:flex;flex-direction:column;align-items:center}
.cover-logo .brand{font-size:1.45em}
.cover-url{position:absolute;bottom:7%;right:6%;color:#fff;font-size:1.05em;font-family:"Montserrat",Arial,sans-serif}

/* back cover */
.back{background:radial-gradient(circle at 40% 45%,#2a4dac 0%,#1a3287 55%,#0f1f5e 100%);color:#fff}
.back-block{position:absolute;left:0;right:0;top:40%;text-align:center;padding:0 30px}
.back-block .brand{justify-content:center;font-size:20px}
.back-block .tagline{margin-top:3px;font-size:8px}
.back-lead{font-size:8.5px;line-height:1.5;margin-top:14px;opacity:.92}
.back-ask{font-family:"Montserrat",Arial,sans-serif;color:#4fb3f0;font-size:17px;margin-top:8px}
.back-phone{font-family:"Montserrat",Arial,sans-serif;font-weight:300;font-size:30px;margin-top:8px;letter-spacing:.02em}
.back-url{font-family:"Montserrat",Arial,sans-serif;color:#4fb3f0;font-size:12px;margin-top:4px}

/* inner text */
.url{position:absolute;font-family:"Montserrat",Arial,sans-serif;font-size:9px;color:var(--navy)}
.rule{position:absolute;height:1px;background:var(--sky)}
.headshot{position:absolute;left:30px;top:86px;width:70px;height:82px;background:linear-gradient(160deg,#c9a58d,#7b5c4c);border:3px solid #fff;box-shadow:0 0 0 1px #ccd}
.shoes-title{position:absolute;left:112px;top:86px;font-family:"Montserrat",Arial,sans-serif;font-size:17px;color:var(--ink);white-space:nowrap}
.shoe{left:112px;top:118px;width:64px;height:30px;border-radius:40% 60% 20% 20%;background:linear-gradient(180deg,#fafafa,#cfcfcf)}
.partner{position:absolute;left:420px;top:92px;font-family:"Open Sans",Arial,sans-serif;font-weight:700;font-size:12px;color:var(--navy);display:flex;align-items:center;gap:5px}
.partner::after{content:"";width:9px;height:9px;border-radius:50%;background:var(--navy)}
.story{position:absolute;left:30px;top:180px;width:480px;font-size:9.5px;line-height:1.5}
.story p{margin-bottom:6px}
.story strong{color:var(--navy)}
.story em{font-weight:700;color:var(--navy)}
.quote-panel{position:absolute;left:0;top:430px;width:330px;height:269px;background:var(--navy);border-top-right-radius:140px 60px}
.quote-panel::before{content:"";position:absolute;left:0;right:0;top:-6px;height:6px;background:var(--sky);border-top-right-radius:140px 10px}
.quotes{position:absolute;left:28px;top:40px;width:250px;color:#fff;font-family:"Montserrat",Arial,sans-serif;font-style:italic;font-weight:600;font-size:10.5px;line-height:1.45}
.quotes p{margin-bottom:12px}
.target{left:230px;top:405px;width:360px;height:360px;border-radius:50%;background:radial-gradient(circle at 40% 35%,#2b5cc4 0%,#16245a 45%,#0b0f22 100%)}

.team{left:0;top:0;width:540px;height:230px;background:linear-gradient(120deg,#6d7488,#c2c6d0 45%,#5b6073 100%)}
.wave{position:absolute;left:0;top:150px}
.bias-title{position:absolute;left:220px;top:248px;font-family:"Montserrat",Arial,sans-serif;font-weight:300;font-size:18px;line-height:1.15;color:var(--ink);text-transform:uppercase}
.bias-list{position:absolute;list-style:none}
.bias-list li{margin-bottom:10px}
.bias-list h3{font-family:"Montserrat",Arial,sans-serif;font-weight:400;font-size:12.5px;color:var(--sky)}
.bias-list p{font-size:8.5px;line-height:1.35;color:var(--ink)}
.bias-list--main{left:220px;top:310px;width:290px}
.bias-list--side{left:30px;top:370px;width:170px}

/* staffing page */
.staff-title{position:absolute;left:30px;top:56px;font-family:"Montserrat",Arial,sans-serif;font-weight:300;font-size:25px;color:var(--navy)}
.staff-note{position:absolute;left:30px;top:96px;width:470px;font-weight:700;font-style:italic;font-size:9.5px;line-height:1.45;color:var(--ink)}
.diff-head{position:absolute;left:30px;top:180px;display:flex;align-items:baseline;gap:8px}
.diff-head .brand{font-size:19px}
.diff-head span{font-family:"Montserrat",Arial,sans-serif;font-weight:300;font-size:19px;color:var(--navy)}
.bullets{position:absolute;font-size:9px;line-height:1.4;color:var(--ink);padding-left:10px}
.bullets li{margin-bottom:3px}
.bullets--a{left:40px;top:232px;width:220px}
.bullets--b{left:290px;top:232px;width:220px}
.ph-1{left:340px;top:430px;width:160px;height:95px;background:linear-gradient(135deg,#5f6777,#d7d9de)}
.ph-2{left:40px;top:480px;width:190px;height:120px;background:linear-gradient(135deg,#3d4352,#9aa0ad)}
.ph-3{left:250px;top:555px;width:170px;height:85px;background:linear-gradient(135deg,#d5d9e0,#6e7687)}

/* how page */
.how{background:linear-gradient(180deg,#e5edf7 0%,#fafcff 60%,#eef3f9 100%)}
.how-head{position:absolute;left:120px;top:28px;display:flex;flex-direction:column}
.how-head .brand{font-size:22px}
.how-head .tagline{font-size:8px;margin-left:110px}
.how-sub{position:absolute;left:180px;top:72px;font-family:"Montserrat",Arial,sans-serif;font-weight:300;font-size:17px;color:var(--navy)}
.step2{position:absolute;left:180px;top:100px;width:360px;height:170px;background:var(--navy);color:#fff;padding:32px 22px 0}
.step1{position:absolute;left:22px;top:130px;width:170px;height:200px;background:var(--sky);color:#fff;padding:16px 14px}
.step-title{font-family:"Montserrat",Arial,sans-serif;font-weight:300;font-size:13px;line-height:1.2;margin-bottom:8px}
.step-text{font-size:8px;line-height:1.45}
.step2 .step-text{margin-top:10px}
.chart{position:absolute;left:30px;top:350px}
.legend{position:absolute;left:102px;top:340px;width:128px;list-style:none;font-size:7px;line-height:1.2;color:var(--muted)}
.legend li{display:flex;align-items:center;gap:5px;margin-bottom:4px}
.legend b{font-family:"Montserrat",Arial,sans-serif;font-weight:400;font-size:13px;color:#9aa5bb;flex:none;width:30px}
.legend .hi b{color:var(--sky)}
.dna{position:absolute;left:245px;width:285px;font-size:8.5px;line-height:1.35}
.dna h4{font-family:"Montserrat",Arial,sans-serif;font-weight:700;font-size:11px;color:var(--sky);margin-bottom:2px}
.dna ul{columns:2;padding-left:10px}
.dna-1{top:285px}.dna-2{top:360px}.dna-3{top:455px}
</style>
</head>
<body>

<!-- single front cover -->
<div class="spread" style="left:420px;top:30px">
  <section class="page" style="width:360px;height:466px;font-size:10px">
    <div class="cover">
      <div class="photo" role="img" aria-label="Photo of three sales professionals reviewing documents in a brick-walled office"></div>
      <div class="cover-band"></div>
      <div class="cover-logo"><span class="brand">Trellwick Partners</span><span class="tagline">Your A.I. Sales Recruiter</span></div>
      <div class="cover-url">www.TrellwickPartners.com</div>
    </div>
  </section>
</div>

<!-- back and front cover spread -->
<div class="spread" style="left:180px;top:530px">
  <section class="page back" style="width:420px;height:544px">
    <div class="back-block">
      <div class="brand brand--light">Trellwick Partners</div>
      <div class="tagline tagline--light">Your A.I. Sales Recruiter</div>
      <p class="back-lead">For explosive growth, nothing moves the needle more than increasing<br>both the quality and quantity of your sales force.<br>So, now you know and we have just one question...</p>
      <p class="back-ask">Would you like our help?</p>
      <p class="back-phone">704-555-0182</p>
      <p class="back-url">www.TrellwickPartners.com</p>
    </div>
  </section>
  <section class="page" style="width:420px;height:544px;font-size:11.7px">
    <div class="cover">
      <div class="photo" role="img" aria-label="Photo of three sales professionals reviewing documents in a brick-walled office"></div>
      <div class="cover-band"></div>
      <div class="cover-logo"><span class="brand">Trellwick Partners</span><span class="tagline">Your A.I. Sales Recruiter</span></div>
      <div class="cover-url">www.TrellwickPartners.com</div>
    </div>
  </section>
</div>

<!-- inner spread: founder and biases -->
<div class="spread" style="left:60px;top:1110px">
  <section class="page" style="width:540px;height:699px">
    <svg class="photo" style="left:0;top:0" width="540" height="80" viewBox="0 0 540 80"><path d="M230 0 H540 V70 C470 20 360 8 230 0Z" fill="var(--navy)"/></svg>
    <div class="photo headshot" role="img" aria-label="Portrait of the founder"></div>
    <h2 class="shoes-title">We have been in your</h2>
    <div class="photo shoe" role="img" aria-label="White sneaker"></div>
    <div class="partner">Corvane</div>
    <div class="story">
      <p>Our founder, <strong>DANIEL RESTREPO</strong> had a sales management career with Corvane spanning over two decades.</p>
      <p>During that time, Daniel had recruited, hired, trained, and when necessary, let go over 2,000 sales people.</p>
      <p>“We are NOT a typical staffing agency, we are an empathetic partner for sales success.”</p>
      <p><em>As a Sales &amp; Marketing consultant, Daniel has helped dozens of companies and learned a common truth.</em></p>
      <p>“Even with tools such as Cultural Fit, DISC, Kestrel Type and others, most companies are just throwing darts in the dark when hiring sales professionals.”</p>
    </div>
    <div class="photo target" role="img" aria-label="Hand pointing a glowing arrow at a target"></div>
    <div class="quote-panel">
      <div class="quotes">
        <p>With decades of experience, Daniel realized that the key to hiring exceptional sales people lay in utilizing an A.I. Predictive Assessment model.</p>
        <p>“Traditional assessments and personality tests only scratch the surface, often missing hidden strengths and weaknesses crucial for predicting sales success.”</p>
        <p>“Compounding the issue is that there are up to 10 unconscious biases present during the interview process.”</p>
      </div>
    </div>
    <div class="url" style="left:395px;top:676px;color:#fff">www.TrellwickPartners.com</div>
  </section>
  <section class="page" style="width:540px;height:699px">
    <div class="photo team" role="img" aria-label="Team of colleagues gathered around a laptop"></div>
    <svg class="wave" width="540" height="90" viewBox="0 0 540 90"><path d="M0 20 C120 90 220 10 330 30 C420 45 480 20 540 0 V90 H0Z" fill="#fff"/><polyline points="150,60 200,40 250,45 300,25" fill="none" stroke="#fff" stroke-width="1.5"/></svg>
    <h2 class="bias-title">Hiring for Sales -<br>10 Unconscious Biases</h2>
    <ul class="bias-list bias-list--side">
      <li><h3>Affinity Bias</h3><p>Favoring candidates who share similar interests</p></li>
      <li><h3>Beauty Bias</h3><p>Impacting judgement on physical appearance</p></li>
      <li><h3>Conformity Bias</h3><p>Preferring a candidate who aligns with existing strategies</p></li>
    </ul>
    <ul class="bias-list bias-list--main">
      <li><h3>Confirmation Bias</h3><p>Preferring a candidate who aligns with existing beliefs</p></li>
      <li><h3>Racial or Ethnic Bias</h3><p>Judgment impacted by stereo types</p></li>
      <li><h3>Gender Bias</h3><p>Decisions based on gender rather than merit</p></li>
      <li><h3>Halo/Horn Bias</h3><p>Letting a single trait disproportionately impact overall impressions</p></li>
      <li><h3>Anchor Bias</h3><p>Relying to heavily on first impressions</p></li>
      <li><h3>Cultural Noise Bias</h3><p>Unintentional favoritism or exclusion based on cultural background</p></li>
      <li><h3>Order Bias</h3><p>Influenced by the sequence of interviews</p></li>
    </ul>
    <div class="rule" style="left:220px;top:660px;width:290px"></div>
    <div class="url" style="left:390px;top:666px">www.TrellwickPartners.com</div>
  </section>
</div>

<!-- inner spread: difference and method -->
<div class="spread" style="left:60px;top:1845px">
  <section class="page" style="width:540px;height:699px">
    <h2 class="staff-title">Traditional Staffing Agencies</h2>
    <p class="staff-note">Recruiters in cubicle farms are typically owned by someone who has never walked in your shoes when hiring salespeople.<br>They also recruit for multiple job positions specializing in a few but not sales.</p>
    <div class="diff-head"><span class="brand">Trellwick Partners</span><span>Is Different</span></div>
    <ul class="bullets bullets--a">
      <li>Founder is a veteran Sales Management Executive</li>
      <li>ONLY sales and sales management recruiting</li>
      <li>A.I. sourcing of active and passive candidates</li>
      <li>Predictive sales assessments 92% accurate</li>
    </ul>
    <ul class="bullets bullets--b">
      <li>Only sourcing the top 20% of the sales talent pool</li>
      <li>STAR certified, unbiased contextual interview questions</li>
      <li>Recorded video of STAR interview for each candidate</li>
      <li>Coaching / Consulting services available after placement</li>
    </ul>
    <svg class="photo" style="left:0;top:0" width="540" height="699" viewBox="0 0 540 699"><path d="M230 560 L300 590 M400 555 L470 480 L495 430" fill="none" stroke="var(--sky)" stroke-width="5"/></svg>
    <div class="photo ph-1" role="img" aria-label="Business team meeting around a table"></div>
    <div class="photo ph-2" role="img" aria-label="Group of business professionals holding tablets"></div>
    <div class="photo ph-3" role="img" aria-label="Colleagues in a bright conference room"></div>
    <div class="url" style="left:380px;top:655px">www.TrellwickPartners.com</div>
    <div class="rule" style="left:30px;top:672px;width:480px"></div>
  </section>
  <section class="page how" style="width:540px;height:699px">
    <div class="how-head"><span class="brand">Trellwick Partners</span><span class="tagline">Your A.I. Sales Recruiter</span></div>
    <div class="step2">
      <p class="step-title">Step 2.<br>Eliminate biases with the worlds #1 sales assessment engine</p>
      <p class="step-text">We assess EVERY candidate regardless of sales experience which screens for <b>21 core sales competencies.</b></p>
    </div>
    <div class="how-sub">How we do it...</div>
    <div class="step1">
      <p class="step-title">Step 1.<br>Understanding the sales candidate mindset</p>
      <p class="step-text">With a robust A.I. talent search engine that crawls through both active AND passive candidates at lightening speed, Trellwick Partners finds talent in minutes, not weeks.</p>
    </div>
    <svg class="chart" width="70" height="70" viewBox="0 0 42 42">
      <circle cx="21" cy="21" r="15.9" fill="none" stroke="#d9e2ef" stroke-width="7"/>
      <circle cx="21" cy="21" r="15.9" fill="none" stroke="var(--sky)" stroke-width="7" stroke-dasharray="45 55" stroke-dashoffset="25"/>
      <circle cx="21" cy="21" r="15.9" fill="none" stroke="var(--royal)" stroke-width="7" stroke-dasharray="15 85" stroke-dashoffset="80"/>
    </svg>
    <ul class="legend">
      <li><b>12%</b>Actively looking for work</li>
      <li><b>13%</b>Casually looking a few times</li>
      <li><b>15%</b>Reaching out to personal network</li>
      <li class="hi"><b>45%</b>Open to talking to a recruiter</li>
      <li class="hi"><b>15%</b>Completely satisfied, not moving</li>
    </ul>
    <div class="dna dna-1"><h4>Will to Sell</h4><ul><li>Desire</li><li>Responsibility</li><li>Commitment</li><li>Motivation</li><li>Outlook</li></ul></div>
    <div class="dna dna-2"><h4>Sales DNA</h4><ul><li>Doesn't Need Approval</li><li>Supportive Beliefs</li><li>Comfortable Discussing Money</li><li>Handles Rejection</li><li>Stays in the Moment</li><li>Supportive Buy Cycle</li></ul></div>
    <div class="dna dna-3"><h4>Tactical</h4><ul><li>Hunting</li><li>Relationship Building</li><li>Selling Value</li><li>Presentation Approach</li><li>Sales Process</li><li>Reaching Decision Makers</li><li>Consultative Selling</li><li>Qualifying</li><li>Closing</li><li>Sales Technology</li></ul></div>
    <div class="url" style="left:390px;top:640px">www.TrellwickPartners.com</div>
    <div class="rule" style="left:30px;top:656px;width:480px"></div>
  </section>
</div>

</body>
</html>
```